7 ¾ long by 5 inches high print ad

I have a 1/2 page ad for a print magazine I need to be designed. Uploaded is the previous year design. We want something to be more aligned with our new website look/feel and new messaging from website.

I have provided some photos, the logo, color codes and a recent banner ad sample for copy.

Target Market(s)

Developers

Font styles to use
Sans Serif

Requirements
Must have
• Clear headline, sub headline, and value statement
• Services to highlight, Tilt-Up Construction,
• Website, phone, social icons, Friendbook, Chirper, and WorkNet
Nice to have
• https://marrowcrestbuilding.com/
• Some of the logos in the clients who trust us section

```html
<!DOCTYPE html>
<html lang="en">
<head>
<meta charset="utf-8">
<title>Marrowcrest Construction – Print Ad</title>
<link href="https://fonts.googleapis.com/css2?family=Arimo:wght@400;700&family=Mulish:wght@400;600&display=swap" rel="stylesheet">
<style>
  :root{
    --navy:#17213f;
    --orange:#d28310;
    --orange-box:#cf7f0a;
    --charcoal:#4a4a4d;
    --light-gray:#c6c6c6;
    --client-gray:#b8b8b8;
    --client-ink:#7d7f80;
    --white:#ffffff;
  }
  *{margin:0;padding:0;box-sizing:border-box}
  html,body{width:1200px;height:775px;overflow:hidden;background:#fff}
  .ad{position:relative;width:1200px;height:775px;font-family:"Arimo",Arial,sans-serif;overflow:hidden}
  .top-band{position:absolute;left:0;top:0;width:1200px;height:31px;background:var(--navy)}
  .header{position:absolute;left:0;top:31px;width:1200px;height:121px;background:var(--white);border-bottom:1.5px solid var(--orange)}
  .brand{position:absolute;left:447px;top:0;display:flex;align-items:flex-start}
  .brand-square{width:52px;height:83px;background:var(--orange)}
  .brand-text{margin-left:22px;margin-top:10px;font-family:"Mulish",sans-serif;color:var(--orange);line-height:1}
  .brand-name{font-size:39px;font-weight:600;letter-spacing:.5px}
  .brand-sub{font-size:20px;font-weight:400;margin-top:3px;margin-left:4px}
  .hero{position:absolute;left:0;top:152px;width:1200px;height:432px;
    background:linear-gradient(180deg,#a9bccb 0%,#c4c9cf 30%,#d9c8c4 42%,#6a6d70 50%,#4f5457 70%,#3e4346 100%)}
  .hero-copy{position:absolute;left:41px;top:26px;color:var(--navy)}
  .hero-kicker{font-size:18px;font-weight:700}
  .hero-headline{font-size:27px;font-weight:700;color:var(--orange);margin-top:4px}
  .hero-sub{font-size:16.5px;margin-top:3px}
  .experience{position:absolute;left:41px;top:340px;color:var(--orange);font-size:18px;line-height:1.3}
  .experience strong{font-size:23px}
  .quality-box{position:absolute;left:429px;top:492px;width:345px;height:92px;background:var(--orange-box);
    color:var(--white);font-size:24px;line-height:1.3;padding:17px 0 0 18px}
  .contact{position:absolute;left:0;top:584px;width:429px;height:129px;background:var(--charcoal);color:var(--white);
    padding:24px 0 0 41px;font-size:19px}
  .contact-row{display:flex;align-items:center;height:32px}
  .contact-row svg{width:22px;height:22px;margin-right:12px;flex:none}
  .social{position:absolute;left:0;top:713px;width:429px;height:62px;background:var(--light-gray);
    display:flex;align-items:center;justify-content:center;gap:12px;font-size:12px;font-weight:700;color:var(--charcoal)}
  .services{position:absolute;left:429px;top:586px;width:345px;height:189px;background:var(--orange-box);
    color:var(--white);padding:18px 0 0 18px;font-size:18px;line-height:30px;list-style:none}
  .clients{position:absolute;left:774px;top:584px;width:426px;height:191px;background:var(--client-gray);padding:20px 0 0 44px}
  .clients-title{font-size:20px;color:#555759}
  .client-grid{display:grid;grid-template-columns:repeat(4,86px);gap:26px 6px;margin-top:28px;
    font-size:13px;font-weight:700;color:var(--client-ink);text-align:center;align-items:center}
</style>
</head>
<body>
<div class="ad">
  <div class="top-band"></div>

  <header class="header">
    <div class="brand">
      <div class="brand-square"></div>
      <div class="brand-text">
        <div class="brand-name">Marrowcrest</div>
        <div class="brand-sub">Construction, Inc.</div>
      </div>
    </div>
  </header>

  <section class="hero" role="img" aria-label="Photo of a tilt-up concrete wall panel being lifted by a crane at dusk on a large construction site, with workers on the slab">
    <div class="hero-copy">
      <p class="hero-kicker">Rising to the challenge since 2003! We love taking on,</p>
      <h1 class="hero-headline">Large scale projects like Tilt Up Construction.</h1>
      <p class="hero-sub">Our Project Management Team is committed to delivering safe, timely and quality workmanship.</p>
    </div>
    <p class="experience">Our collective commercial experience<br>at <strong>Marrowcrest Construction</strong><br>span over 100 years.</p>
  </section>

  <div class="quality-box">Quality Service &amp;<br>Expert Workmanship</div>

  <section class="contact">
    <div class="contact-row">
      <svg viewBox="0 0 24 24" fill="#fff"><path d="M12 5c-5 0-10 1.5-10 4.5V11h5V9h10v2h5V9.5C22 6.5 17 5 12 5zM7 12l-2 7h14l-2-7H7zm5 1.5a2.5 2.5 0 1 1 0 5 2.5 2.5 0 0 1 0-5z"/></svg>
      916.555.0142
    </div>
    <div class="contact-row">
      <svg viewBox="0 0 24 24" fill="none" stroke="#fff" stroke-width="2"><rect x="3" y="5" width="18" height="14" rx="1"/><path d="M3 6l9 7 9-7"/></svg>
      info@marrowcrestbuilding.com
    </div>
    <div class="contact-row">
      <svg viewBox="0 0 24 24" fill="none" stroke="#fff" stroke-width="1.8"><circle cx="12" cy="12" r="9"/><ellipse cx="12" cy="12" rx="4" ry="9"/><path d="M3 12h18M5 7h14M5 17h14"/></svg>
      marrowcrestbuilding.com
    </div>
  </section>

  <nav class="social">
    <span>Friendbook</span><span>Searchly</span><span>WorkNet</span><span>Chirper</span><span>Reviewly</span><span>ClipTube</span>
  </nav>

  <ul class="services">
    <li>Commercial New Construction</li>
    <li>Strip Mall Renovation</li>
    <li>Office Park Builder</li>
    <li>Tilt-Up Construction</li>
    <li>Construction Consulting &amp; Planning</li>
  </ul>

  <section class="clients">
    <h2 class="clients-title" style="font-weight:400">Clients Who Trust Us</h2>
    <div class="client-grid">
      <span>Hearthloaf</span><span>Pinecrest Grill</span><span>Fieldline Sports</span><span>Trail Scouts</span>
      <span>Six Brothers</span><span>Ridgeway</span><span>Value &amp; Fresh</span><span>Harbor Rack</span>
    </div>
  </section>
</div>
</body>
</html>
```